Pharmaceutical Manufacturing Services Advertisement

We need a new full page advertisement designed for publication in international magazines. We are a custom pharmaceutical manufacturing company and we help biotechnology companies scale up their drug development for clinical trials. The products we help manufacture are therapeutics for global healthcare problems.

Target Market(s)

Verane Bio is a privately owned contract development manufacturing organisation (CDMO) headquartered in Kellow, QLD, Australia.

Our mission is to is to be a global leader in development and in the provision of contract manufacturing for active pharmaceutical ingredient processes.

Why we do what we Do:

To help advance Biotechnology Companies so that they can deliver innovative therapeutics
~ enabling patients to live longer, healthier and happier lives
~ which solves worldwide health problems

Verane Bio’s role is to develop, implement and scale up the production to deliver biologic medicines for patients in partnership with the biotechnology companies.

Industry/Entity Type

Biotechnology

Font styles to use
Sans Serif

Colors

Designer to choose colors to be used in the design.

Requirements
Must have
• Please see the script on the Word document. There are 4 optional Header Taglines. Additional ideas for multiple designs for the taglines welcomed.
• However preference is for either of the first two:
• 1. Building your vision for better healthcare
• 2. Bridging your vision for better healthcare
• File Specs:
• • All artwork should be submitted as high-resolution (300 min. dpi), press-ready PDF files
• • CMYK color only
• • Full page 8.25” x 10.812”; 209.55 x 274.62 mm
• • Live Area for all sizes: 0.25” (6.35 mm) inside the trim
• • Bleed Area for all sizes: Extends 0.125” (3.175 mm) from trim
Nice to have
• Modern Science look to inspire biotechnology companies to work with us.
• Search for images to use by keyword "recombinant dna"

```html
<!DOCTYPE html>
<html lang="en">
<head>
<meta charset="utf-8">
<title>Verane Bio – Full Page Advertisement</title>
<link rel="stylesheet" href="https://fonts.googleapis.com/css2?family=Oswald:wght@400;500&family=Roboto+Condensed:wght@500&family=Source+Sans+3:wght@400;600&display=swap">
<style>
  :root {
    --navy: #0d3a5c;
    --navy-deep: #0a2f4b;
    --lime: #a9bd36;
    --lime-light: #b7c94a;
    --ink: #3a3a3a;
    --paper: #ffffff;
    --stage: #e4e4e4;
  }
  * { box-sizing: border-box; margin: 0; padding: 0; }
  html, body { width: 1003px; height: 1200px; overflow: hidden; }
  body { background: var(--stage); font-family: "Source Sans 3", sans-serif; color: var(--ink); }

  .advert {
    position: absolute; left: 81px; top: 30px;
    width: 840px; height: 1140px;
    background: var(--paper); overflow: hidden;
  }
  .hero { position: absolute; left: 0; top: 0; width: 840px; height: 600px; display: block; }

  .headline {
    position: absolute; left: 26px; top: 38px;
    font-family: "Oswald", sans-serif; font-weight: 500;
    font-size: 35px; line-height: 42px; color: var(--paper);
    text-transform: uppercase; letter-spacing: 0.3px;
  }
  .brand {
    position: absolute; left: 560px; top: 130px;
    display: flex; align-items: center; gap: 10px;
  }
  .brand-dot { width: 14px; height: 14px; border-radius: 50%; background: var(--lime); }
  .brand-name {
    font-family: "Oswald", sans-serif; font-weight: 500;
    font-size: 44px; color: var(--navy); letter-spacing: 1px; text-transform: uppercase;
  }

  .intro { position: absolute; left: 26px; top: 598px; width: 790px; }
  .intro-title {
    font-family: "Roboto Condensed", sans-serif; font-weight: 500;
    font-size: 24px; line-height: 29px; color: var(--lime); text-transform: uppercase;
    margin-bottom: 10px;
  }
  .intro p { font-size: 16px; line-height: 19.5px; text-align: justify; margin-bottom: 13px; }

  .offer { position: absolute; top: 842px; width: 392px; height: 200px;
    border-radius: 12px; background: var(--lime); overflow: hidden;
    box-shadow: 0 3px 8px rgba(0,0,0,0.25); }
  .offer-products { left: 30px; }
  .offer-services { left: 432px; }
  .offer-title {
    height: 50px; background: var(--navy); color: var(--paper);
    font-family: "Source Sans 3", sans-serif; font-weight: 600; font-size: 21px;
    text-align: center; line-height: 52px; text-transform: uppercase;
    border-radius: 12px 12px 0 0;
  }
  .offer-list { list-style: none; padding: 12px 0 0 28px; }
  .offer-list li {
    position: relative; padding-left: 22px;
    font-size: 17px; line-height: 26px; color: var(--paper);
  }
  .offer-list li::before {
    content: ""; position: absolute; left: 0; top: 7px;
    width: 12px; height: 12px; border-radius: 50%; background: var(--navy);
  }
  .offer-list li::after {
    content: ""; position: absolute; left: 3px; top: 10.5px;
    width: 4px; height: 4px; border-top: 1.5px solid var(--paper); border-right: 1.5px solid var(--paper);
    transform: rotate(45deg);
  }

  .footer { position: absolute; left: 0; top: 1055px; width: 840px; height: 85px; }
  .footer-bar { position: absolute; left: 0; top: 0; width: 840px; height: 85px; display: block; }
  .phone {
    position: absolute; left: 40px; top: 14px;
    display: flex; align-items: center; gap: 18px;
    font-family: "Oswald", sans-serif; font-weight: 500; font-size: 38px; color: var(--paper);
  }
  .contact {
    position: absolute; right: 56px; top: 44px;
    font-size: 18px; color: var(--paper); letter-spacing: 0.4px;
  }
</style>
</head>
<body>
<main class="advert">
  <svg class="hero" viewBox="0 0 840 600" xmlns="http://www.w3.org/2000/svg">
    <defs>
      <linearGradient id="labTone" x1="0" y1="0" x2="1" y2="1">
        <stop offset="0" stop-color="#6f93ad"/>
        <stop offset="0.5" stop-color="#b9cedc"/>
        <stop offset="1" stop-color="#4f7895"/>
      </linearGradient>
    </defs>
    <rect x="0" y="100" width="840" height="480" fill="url(#labTone)" role="img" aria-label="Laboratory scientist in protective gear using a holographic medical data interface"/>
    <path d="M0 0 H840 V70 C720 40 600 70 520 120 C420 170 220 165 0 145 Z" fill="var(--navy)"/>
    <path d="M0 145 C220 165 420 172 520 122" fill="none" stroke="var(--lime)" stroke-width="4"/>
    <path d="M505 130 C600 72 720 50 840 68 V300 C740 320 600 290 505 130 Z" fill="var(--paper)"/>
    <path d="M0 528 C280 476 580 466 840 488" fill="none" stroke="var(--lime)" stroke-width="3"/>
    <path d="M0 538 C280 488 580 478 840 498 V532 C580 518 300 540 0 588 Z" fill="var(--navy)"/>
    <path d="M0 588 C300 540 580 518 840 532 V600 H0 Z" fill="var(--paper)"/>
  </svg>

  <h1 class="headline">Building your vision for<br>better healthcare</h1>

  <div class="brand">
    <span class="brand-dot"></span>
    <span class="brand-name">Verane Bio</span>
  </div>

  <section class="intro">
    <h2 class="intro-title">Your partner in early<br>phase clinical biomanufacturing</h2>
    <p>We have been serving the pharmaceutical, biotechnology and veterinary industry for over 20 years so you can create innovative medicines for worldwide health problems.</p>
    <p>Get your therapeutics to the patient faster with cost-effective manufacturing for your GMP clinical trial material. We offer rapid technology transfer, scale-up development and manufacturing of microbial cell-derived proteins at up to 500L scale. We prepare your active pharmaceutical ingredient (API) products to a world class standard ready for clinical development.</p>
  </section>

  <section class="offer offer-products">
    <h3 class="offer-title">Products</h3>
    <ul class="offer-list">
      <li>Recombinant proteins</li>
      <li>Live Biotherapeutics</li>
      <li>Bacterial vaccines</li>
      <li>Plasmid DNA</li>
    </ul>
  </section>

  <section class="offer offer-services">
    <h3 class="offer-title">Services</h3>
    <ul class="offer-list">
      <li>Bacterial / Yeast Fermentation</li>
      <li>Cell Banking</li>
      <li>Process Development/Scale-up</li>
      <li>cGMP Manufacture of biopharmaceutical APIs</li>
      <li>Stability Testing</li>
    </ul>
  </section>

  <footer class="footer">
    <svg class="footer-bar" viewBox="0 0 840 85" xmlns="http://www.w3.org/2000/svg">
      <rect x="0" y="29" width="840" height="56" fill="var(--navy)"/>
      <path d="M0 0 H382 L405 85 H0 Z" fill="var(--lime)"/>
    </svg>
    <div class="phone">
      <svg width="26" height="44" viewBox="0 0 26 44" xmlns="http://www.w3.org/2000/svg" aria-hidden="true">
        <rect x="2" y="2" width="22" height="40" rx="4" fill="none" stroke="#fff" stroke-width="3"/>
        <line x1="2" y1="9" x2="24" y2="9" stroke="#fff" stroke-width="2"/>
        <line x1="2" y1="34" x2="24" y2="34" stroke="#fff" stroke-width="2"/>
      </svg>
      <span>+61 (7) 3400 5182</span>
    </div>
    <div class="contact">veranebio.com.au | enquiries@veranebio.com.au</div>
  </footer>
</main>
</body>
</html>
```